Webpage Design_Telecommunications VOIP

BRV Linkworks Inc. Talk Made Simple.
Webpage/Homepage Design for Voiceover IP solution and Telecommunications company, looking to expand market and compete with larger providers.
He has a long standing local provider business with http://www.harborlane-example.com/ (You can see the logo there, blue cloud, phone pad) with tag Line: talk made simple in first rotation. You can also find layout and content for voiceover IP services, which is the focus for BRV Linkworks, so it can stand alone from Harborlane.

Target Market(s)

Malls, Doctors Offices, Retail, Hospitals, Car Dealers, Finance Services, HR Services, Insurance, Hotels, Travel Commerce, Government, Software Companies, Large Health Clubs/Country Clubs, Entertainment Venues, Quarrow Arena, Maplecrest Pines University/Colleges/Education.
See Product list on Talo (also Site inspiration) they set their site up based on different verticals, just to give you some inspiration.
http://talo-example.com/small-business/
http://talo-example.com/government/

Industry/Entity Type

Telecommunications

Number of Pages Required

1 page

Font styles to use
Sans Serif

Requirements
Must have
• Logo, Clean, Simple Strong Highlight services Navigation.
• Similar, competitive and current design like http://talo-example.com/
• Strong theme of Customer Service, but with modern competitive messaging.
• Fast, simple communication solutions/messages.
• Use of the Phone in the cloud graphic as an interactive feature.
• Contact form
• Pixelvault Image ID: 508342716
• Image ID: 634910275
• Image ID: 172605943
Nice to have
• Quick Service boxes for "PRICING" (to be supported with a smart form on our end)
Should not have
• Generic Images, of Professionals shaking hands, please chose images less expected.

```html
<!DOCTYPE html>
<html lang="en">
<head>
<meta charset="utf-8">
<title>BRV Linkworks – Talk Made Simple</title>
<link href="https://fonts.googleapis.com/css2?family=Roboto:wght@300;400;500;700&display=swap" rel="stylesheet">
<style>
:root{
  --blue:#4a90d9;
  --blue-light:#6aaee4;
  --navy:#2c3e52;
  --ink:#2b2b2b;
  --muted:#666;
  --topbar:#efefef;
  --page:#f4f4f4;
  --white:#fff;
  --footer:#323232;
}
*{margin:0;padding:0;box-sizing:border-box}
html,body{width:720px;height:1200px;overflow:hidden;background:var(--white)}
body{font-family:'Roboto',sans-serif;color:var(--ink);position:relative}
.abs{position:absolute}

.topbar{left:0;top:0;width:720px;height:24px;background:var(--topbar);font-size:9px;color:#333}
.topbar .contact{top:7px;display:flex;align-items:center;gap:5px}
.topbar .contact svg{width:8px;height:8px}
.topbar .social{right:54px;top:7px;display:flex;gap:4px}
.topbar .social span{width:10px;height:10px;background:var(--blue);border-radius:2px;display:block}

.header{left:0;top:24px;width:720px;height:67px;background:var(--white);border-bottom:1px solid #e4e4e4}
.brand{left:54px;top:20px;display:flex;align-items:center;gap:8px}
.brand .dot{width:26px;height:26px;border-radius:50%;background:var(--blue)}
.brand .name{font-size:17px;font-weight:500;color:var(--ink);letter-spacing:.3px;line-height:1}
.brand .tag{font-size:7.5px;color:#444;letter-spacing:.3px;margin-top:2px}
.nav{right:54px;top:27px;display:flex;align-items:center}
.nav a{font-size:8.5px;color:#222;text-decoration:none;padding:6px 12px;letter-spacing:.2px}
.nav a.active{color:var(--blue);border:1px solid var(--blue);padding:6px 11px;margin-right:4px}

.hero{left:0;top:91px;width:720px;height:317px;background:linear-gradient(180deg,#c9ced3 0%,#dfe2e4 45%,#eef0f1 70%,#dadcde 100%)}
.hero .photo{left:60px;top:60px;width:370px;height:240px;border-radius:50%;background:radial-gradient(ellipse at 50% 45%,rgba(46,50,54,.9) 0%,rgba(61,66,71,.6) 45%,rgba(60,64,70,0) 72%)}
.hero .mark{left:474px;top:203px;display:flex;align-items:center;gap:8px}
.hero .mark .dot{width:34px;height:34px;border-radius:50%;background:var(--blue-light)}
.hero .mark .name{font-size:22px;font-weight:500;color:#111;letter-spacing:.3px;line-height:1}
.hero .mark .tag{font-size:12px;color:#222;margin-top:2px}
.hero .arrows{left:54px;top:268px;display:flex;gap:3px}
.hero .arrows span{width:20px;height:20px;border-radius:50%;background:#9a9ea2;display:flex;align-items:center;justify-content:center}
.hero .arrows svg{width:8px;height:8px}

.welcome{left:0;top:408px;width:720px;height:288px;background:var(--page)}
.welcome h1{position:absolute;left:0;width:720px;top:30px;text-align:center;font-size:19px;font-weight:400;color:#333;letter-spacing:.2px}
.welcome h1 span{color:var(--blue)}
.welcome .lead{position:absolute;left:58px;width:604px;top:60px;text-align:center;font-size:7.2px;line-height:13.6px;color:var(--muted)}
.service{width:170px;text-align:center;top:133px}
.service .ring{width:60px;height:60px;border-radius:50%;border:1.2px solid #444;margin:0 auto;display:flex;align-items:center;justify-content:center}
.service .ring svg{width:20px;height:20px}
.service h2{font-size:10.5px;font-weight:400;color:var(--blue);margin-top:17px;letter-spacing:.2px}
.service p{font-size:7.2px;line-height:10.5px;color:#444;margin-top:7px}

.pricing{left:0;top:696px;width:720px;height:222px;background:linear-gradient(180deg,#6eb0e6 0%,#4d91d4 100%);color:var(--white)}
.pricing h2{position:absolute;left:0;width:720px;top:23px;text-align:center;font-size:15.5px;font-weight:400;letter-spacing:.3px}
.pricing .sub{position:absolute;left:0;width:720px;top:45px;text-align:center;font-size:12px;font-weight:300}
.plan{top:80px;width:118px;height:110px;text-align:center}
.plan.featured{background:var(--navy);border:1.5px solid #1c2a38;box-shadow:0 2px 6px rgba(0,0,0,.3)}
.plan .pname{font-size:11px;font-weight:300;margin-top:16px;padding-bottom:9px;border-bottom:1px solid rgba(255,255,255,.5);margin-left:20px;margin-right:20px}
.plan .users{font-size:11px;font-weight:300;margin-top:10px;padding-bottom:7px;border-bottom:1px solid rgba(255,255,255,.5);margin-left:20px;margin-right:20px}
.plan .price{font-size:20px;font-weight:300;margin-top:5px}
.plan .price small{font-size:10px}
.plan .per{font-size:7.5px;margin-top:1px;padding-left:36px}
.divider{top:84px;width:1px;height:106px;background:rgba(255,255,255,.6)}

.news{left:0;top:918px;width:720px;height:162px;background:var(--page)}
.news h2{position:absolute;left:55px;top:26px;font-size:11.5px;font-weight:400;color:#222}
.news h2 span{color:var(--blue)}
.news .ctrl{right:54px;top:26px;font-size:11px;color:#222}
.card{top:54px;width:300px;display:flex;gap:10px}
.card .thumb{width:128px;height:80px;border:3px solid var(--white);box-shadow:0 0 2px rgba(0,0,0,.25);flex:none}
.card h3{font-size:7.5px;font-weight:400;color:var(--blue);margin-top:3px}
.card .date{font-size:6.2px;color:#666;margin-top:6px}
.card p{font-size:5.6px;line-height:10.2px;color:#555;margin-top:5px}
.card .more{font-size:6.5px;color:#222;margin-top:6px}

.partners{left:0;top:1080px;width:720px;height:62px;background:var(--white);display:flex;justify-content:space-around;align-items:center;padding:0 50px}
.partners span{display:flex;align-items:center;gap:5px;font-size:14px;font-weight:400;color:#3a3a3a}
.partners span i{width:14px;height:14px;border-radius:50%;background:#555;display:block}

.footer{left:0;top:1142px;width:720px;height:58px;background:var(--footer);color:#e8e8e8}
.footer .links{left:54px;top:17px;font-size:7.2px}
.footer .copy{left:54px;top:32px;font-size:7.2px}
.footer .social{right:70px;top:14px;display:flex;gap:3px}
.footer .social span{width:24px;height:24px;border-radius:50%;border:1px solid #ddd;display:block}
</style>
</head>
<body>

<div class="abs topbar">
  <div class="abs contact" style="left:54px">
    <svg viewBox="0 0 10 10"><path fill="#4a90d9" d="M2 1l2 2-1 1.3c.6 1.2 1.5 2.1 2.7 2.7L7 6l2 2-1.2 1.5C4.5 9.3.7 5.5.5 2.2z"/></svg>
    <span>+654 31 402 118</span>
  </div>
  <div class="abs contact" style="left:151px">
    <svg viewBox="0 0 10 10"><rect x="0.5" y="2" width="9" height="6.5" fill="#4a90d9"/><path d="M0.5 2l4.5 3.5L9.5 2" stroke="#fff" fill="none" stroke-width=".8"/></svg>
    <span>info@brvlinkworks-example.com</span>
  </div>
  <div class="abs social"><span></span><span></span><span></span><span></span></div>
</div>

<header class="abs header">
  <div class="abs brand">
    <div class="dot"></div>
    <div>
      <div class="name">BRV LINKWORKS</div>
      <div class="tag">talk made simple</div>
    </div>
  </div>
  <nav class="abs nav">
    <a class="active" href="#">HOME</a>
    <a href="#">ABOUT US</a>
    <a href="#">PRODUCTS</a>
    <a href="#">PARNERS</a>
    <a href="#">SUPPORT</a>
    <a href="#">CONTACTS</a>
  </nav>
</header>

<section class="abs hero" role="img" aria-label="Desk phone with headset in front of a blurred city skyline">
  <div class="abs photo"></div>
  <div class="abs mark">
    <div class="dot"></div>
    <div>
      <div class="name">BRV LINKWORKS</div>
      <div class="tag">talk made simple</div>
    </div>
  </div>
  <div class="abs arrows">
    <span><svg viewBox="0 0 8 8"><path d="M5.5 1L2.5 4l3 3" stroke="#fff" fill="none" stroke-width="1.3"/></svg></span>
    <span><svg viewBox="0 0 8 8"><path d="M2.5 1l3 3-3 3" stroke="#fff" fill="none" stroke-width="1.3"/></svg></span>
  </div>
</section>

<section class="abs welcome">
  <h1>WELCOME TO <span>BRV LINKWORKS</span></h1>
  <p class="lead">Lorem Ipsum has been the industry's standard dummy text ever since the 1500s, when an unknown printer took a galley of type and scrambled it to make a type specimen book. It has survived not only five centuries, but also the leap into electronic typesetting, remaining essentially unchanged. It was popularised in the 1960s with the release of Typemark sheets containing Lorem Ipsum passages, and more recently with desktop publishing software like Layoutry Pro including versions of Lorem Ipsum.</p>

  <div class="abs service" style="left:72px">
    <div class="ring"><svg viewBox="0 0 20 20"><rect x="7" y="2" width="6" height="10" rx="3" fill="#4a90d9"/><path d="M5 9a5 5 0 0 0 10 0M10 14v4M7 18h6" stroke="#4a90d9" stroke-width="1.5" fill="none"/></svg></div>
    <h2>VOICEOVER IP SOLUTION</h2>
    <p>Lorem Ipsum has been the industry's standard dummy text ever since the 1500s, when an unknown printer took a galley</p>
  </div>
  <div class="abs service" style="left:274px">
    <div class="ring"><svg viewBox="0 0 20 20"><rect x="3" y="5" width="14" height="12" rx="2" fill="#4a90d9"/><rect x="8" y="2" width="7" height="5" fill="#4a90d9"/><g fill="#fff"><rect x="9" y="9" width="2" height="2"/><rect x="12" y="9" width="2" height="2"/><rect x="9" y="12" width="2" height="2"/><rect x="12" y="12" width="2" height="2"/><rect x="5" y="8" width="2" height="7"/></g></svg></div>
    <h2>TELECOMMUNICATIONS</h2>
    <p>Lorem Ipsum has been the industry's standard dummy text ever since the 1500s, when an unknown printer took a galley</p>
  </div>
  <div class="abs service" style="left:476px">
    <div class="ring"><svg viewBox="0 0 20 20"><g stroke="#4a90d9" stroke-width="2" fill="none" stroke-linecap="round"><path d="M2 8a11 11 0 0 1 16 0"/><path d="M5 11a7 7 0 0 1 10 0"/><path d="M8 14a3 3 0 0 1 4 0"/></g><circle cx="10" cy="16.5" r="1.3" fill="#4a90d9"/></svg></div>
    <h2>NETWORKS</h2>
    <p>Lorem Ipsum has been the industry's standard dummy text ever since the 1500s, when an unknown printer took a galley</p>
  </div>
</section>

<section class="abs pricing">
  <h2>STANDARD PRICING</h2>
  <div class="sub">Quick Service</div>

  <div class="abs plan" style="left:60px"><div class="pname">SERVICE 1</div><div class="users">1-4 USERS</div><div class="price">$29<small>.95</small></div><div class="per">Per Device</div></div>
  <div class="abs plan featured" style="left:178px"><div class="pname">SERVICE 2</div><div class="users">5-9 USERS</div><div class="price">$25<small>.95</small></div><div class="per">Per Device</div></div>
  <div class="abs plan" style="left:300px"><div class="pname">SERVICE 3</div><div class="users">10-24 USERS</div><div class="price">$23<small>.95</small></div><div class="per">Per Device</div></div>
  <div class="abs divider" style="left:417px"></div>
  <div class="abs plan" style="left:419px"><div class="pname">SERVICE 4</div><div class="users">25-49 USERS</div><div class="price">$21<small>.95</small></div><div class="per">Per Device</div></div>
  <div class="abs divider" style="left:535px"></div>
  <div class="abs plan" style="left:537px"><div class="pname">SERVICE 5</div><div class="users">50-100 USERS</div><div class="price">$19<small>.95</small></div><div class="per">Per Device</div></div>
</section>

<section class="abs news">
  <h2>LATEST <span>NEWS</span></h2>
  <div class="abs ctrl">&lsaquo;&thinsp;&rsaquo;</div>
  <article class="abs card" style="left:55px">
    <div class="thumb" role="img" aria-label="Server room corridor with rows of racks" style="background:linear-gradient(90deg,#2a3440,#8ea2b4 50%,#2d3946)"></div>
    <div>
      <h3>SIMPLY DUMMY TEXT</h3>
      <div class="date">20/08/2015</div>
      <p>Lorem Ipsum has been the industry's standard dummy text ever since the 1500s, when an unknown printer took a galley of type and scrambled it to make a type specimen book.</p>
      <div class="more">Read More &gt;&gt;</div>
    </div>
  </article>
  <article class="abs card" style="left:373px">
    <div class="thumb" role="img" aria-label="VOIP concept drawn on a blue sky background" style="background:linear-gradient(180deg,#3f8fdc,#7fc0ee)"></div>
    <div>
      <h3>SIMPLY DUMMY TEXT</h3>
      <div class="date">20/08/2015</div>
      <p>Lorem Ipsum has been the industry's standard dummy text ever since the 1500s, when an unknown printer took a galley of type and scrambled it to make a type specimen book.</p>
      <div class="more">Read More &gt;&gt;</div>
    </div>
  </article>
</section>

<section class="abs partners">
  <span><i></i>Pressly</span>
  <span><i></i>Tandemo</span>
  <span><i></i>Cartwell</span>
  <span><i></i>Dropline</span>
  <span><i></i>Quickscript</span>
</section>

<footer class="abs footer">
  <div class="abs links">Privacy policy &nbsp;/&nbsp; Cookie policy &nbsp;/&nbsp; Sitemap / Terms &amp; Conditions</div>
  <div class="abs copy">Copyright © 2016. All Rights Reserved</div>
  <div class="abs social"><span></span><span></span><span></span><span></span></div>
</footer>

</body>
</html>
```